Bref créative
BrindleWorks Stationery
Package
Use same font as used in my logo
Myriad
Professional
Marc T. Delvaux
Founder
418 Quarry Lane
Alder Falls, VT 05987
marc.delvaux@brindleworks-mail.com
www.brindleworks-mail.com

```html
<!DOCTYPE html>
<html lang="en">
<head>
<meta charset="utf-8">
<title>BrindleWorks Business Cards</title>
<link rel="stylesheet" href="https://fonts.googleapis.com/css2?family=Source+Sans+3:wght@400;600;700&display=swap">
<style>
  :root {
    --canvas: #2b2b2b;
    --card-dark: #0c0c0c;
    --card-dark-edge: #1c1c1c;
    --card-light: #ffffff;
    --ink: #222222;
    --ink-soft: #444444;
    --accent-blue: #2c6aa3;
    --badge-ring: #d8d8d8;
    --badge-fill: #3a3a3a;
    --muted-light: #8a8a8a;
  }
  * { margin: 0; padding: 0; box-sizing: border-box; }
  html, body {
    width: 1200px;
    height: 901px;
    overflow: hidden;
    background: var(--canvas);
    font-family: "Source Sans 3", "Myriad Pro", Arial, sans-serif;
  }
  .stage {
    position: relative;
    width: 1200px;
    height: 901px;
  }
  .card {
    position: absolute;
    left: 290px;
    width: 620px;
    height: 354px;
    border-radius: 26px;
    overflow: hidden;
  }
  /* Back side */
  .card--back {
    top: 66px;
    background: linear-gradient(160deg, var(--card-dark-edge) 0%, var(--card-dark) 60%);
  }
  .back-badge {
    position: absolute;
    left: 50%;
    top: 122px;
    width: 96px;
    height: 96px;
    margin-left: -48px;
    border-radius: 50%;
    background: var(--badge-fill);
    border: 3px solid var(--badge-ring);
  }
  .back-url {
    position: absolute;
    left: 0;
    right: 0;
    top: 234px;
    text-align: center;
    color: var(--muted-light);
    font-size: 11px;
    letter-spacing: 2px;
  }
  /* Front side */
  .card--front {
    top: 478px;
    background: var(--card-light);
  }
  .brand {
    position: absolute;
    left: 34px;
    top: 44px;
    display: flex;
    align-items: center;
    gap: 12px;
  }
  .brand-dot {
    width: 46px;
    height: 46px;
    border-radius: 50%;
    background: var(--ink);
  }
  .brand-name {
    font-size: 50px;
    font-weight: 600;
    color: var(--ink);
    letter-spacing: -0.5px;
    line-height: 1;
  }
  .contact {
    position: absolute;
    left: 322px;
    top: 150px;
    color: var(--ink-soft);
    font-size: 15px;
    line-height: 1.3;
  }
  .contact-name {
    color: var(--accent-blue);
    font-size: 19px;
    font-weight: 700;
  }
  .contact-role { margin-bottom: 12px; }
  .contact-address { margin-bottom: 8px; }
  .contact-line {
    display: flex;
    align-items: center;
    gap: 7px;
  }
  .contact-line svg { width: 13px; height: 13px; flex: none; }
</style>
</head>
<body>
<main class="stage">
  <section class="card card--back" aria-label="Card back">
    <div class="back-badge" role="img" aria-label="BrindleWorks emblem"></div>
    <p class="back-url">www.brindleworks-mail.com</p>
  </section>

  <section class="card card--front" aria-label="Card front">
    <div class="brand">
      <span class="brand-dot"></span>
      <span class="brand-name">BrindleWorks</span>
    </div>
    <div class="contact">
      <p class="contact-name">Marc T. Delvaux</p>
      <p class="contact-role">Founder</p>
      <p>418 Quarry Lane</p>
      <p class="contact-address">Alder Falls, VT 05987</p>
      <p class="contact-line">
        <svg viewBox="0 0 12 12" aria-hidden="true"><path d="M2 1h2.5l1 2.5-1.5 1a6 6 0 0 0 3.5 3.5l1-1.5 2.5 1V10a1 1 0 0 1-1 1A9 9 0 0 1 1 2a1 1 0 0 1 1-1z" fill="#444"/></svg>
        555-318-0142
      </p>
      <p class="contact-line">
        <svg viewBox="0 0 12 12" aria-hidden="true"><rect x="1" y="2.5" width="10" height="7" fill="none" stroke="#444" stroke-width="1.2"/><path d="M1 2.5l5 4 5-4" fill="none" stroke="#444" stroke-width="1.2"/></svg>
        marc.delvaux@brindleworks-mail.com
      </p>
      <p class="contact-line">
        <svg viewBox="0 0 12 12" aria-hidden="true"><circle cx="6" cy="6" r="5" fill="none" stroke="#444" stroke-width="1.2"/><ellipse cx="6" cy="6" rx="2.2" ry="5" fill="none" stroke="#444" stroke-width="1"/><path d="M1 6h10" stroke="#444" stroke-width="1"/></svg>
        www.brindleworks-mail.com
      </p>
    </div>
  </section>
</main>
</body>
</html>
```